Property Management Special Flyer - this month only deal

We need a flyer that's design aligns with the style of our website and regular price package attached.
We are a high quality service company that offers property management along Sydney's Northern Beaches.
This month we want to offer a deal where we are waiving Advertising Fees and a special management rate of 5% for this month (Aug) only.
Please show all the same details as on the "Tenure and Oversight Bundle" flyer but advertising the fact that this month only we are waiving the $350 advertising fee and a special Management fee of 5%.
I would like an A4 print ready version (with bleed if nec), an PDF version so we can email it to clients and an editable Photoshop PSD layered file so we can edit text if necessary for future use.
We would like to use the same background image as used in the price package flyer attached (background image also attached)
We want this flyer to capture attention but still look professional and clean like our website.

```html
<!DOCTYPE html>
<html lang="en">
<head>
<meta charset="utf-8">
<title>Tenure and Oversight Bundle</title>
<link href="https://fonts.googleapis.com/css2?family=Lato:ital,wght@0,300;0,400;0,700;1,400;1,700&family=Oswald:wght@500;600&display=swap" rel="stylesheet">
<style>
  :root {
    --teal: #1f93a0;
    --teal-deep: #0f6f7b;
    --teal-text: #1c7f8c;
    --ink: #2f3336;
    --charcoal: #3b3e41;
    --black: #1a1b1c;
    --white: #ffffff;
    --page: #eceeef;
  }
  * { margin: 0; padding: 0; box-sizing: border-box; }
  html, body { width: 869px; height: 1200px; overflow: hidden; background: var(--page); }
  .flyer {
    position: relative; width: 869px; height: 1200px; overflow: hidden;
    background: var(--white); font-family: "Lato", Arial, sans-serif; color: var(--ink);
  }
  .flyer-shapes { position: absolute; inset: 0; }
  .brand {
    position: absolute; top: 62px; right: 30px;
    font-family: "Lato", Arial, sans-serif; font-weight: 700; font-size: 30px;
    color: var(--white); letter-spacing: 0.5px; display: flex; align-items: center; gap: 10px;
  }
  .brand-dot { width: 14px; height: 14px; border-radius: 50%; background: var(--white); }
  .title { position: absolute; left: 27px; top: 448px; }
  .title-main {
    font-family: "Oswald", Impact, sans-serif; font-weight: 600; font-size: 62px;
    line-height: 1; color: var(--white); letter-spacing: 0.5px;
  }
  .title-sub {
    font-family: "Lato", Arial, sans-serif; font-weight: 300; font-size: 40px;
    line-height: 1.1; color: var(--ink); margin-top: 6px; letter-spacing: 0.3px;
  }
  .includes-heading {
    position: absolute; left: 20px; top: 582px;
    font-family: "Oswald", Impact, sans-serif; font-weight: 500; font-size: 25px;
    color: var(--teal-text); letter-spacing: 0.5px;
  }
  .includes-list { position: absolute; list-style: none; }
  .includes-list li {
    position: relative; padding-left: 20px; margin-bottom: 4px;
    font-style: italic; font-size: 13.5px; line-height: 17px; color: var(--ink);
  }
  .includes-list li::before {
    content: ""; position: absolute; left: 2px; top: 3px; width: 7px; height: 7px;
    border-right: 3px solid var(--teal); border-top: 3px solid var(--teal); transform: rotate(45deg);
  }
  .col-1 { left: 27px; top: 626px; width: 190px; }
  .col-2 { left: 329px; top: 627px; width: 200px; }
  .col-3 { left: 661px; top: 629px; width: 190px; }
  .rates { position: absolute; left: 27px; top: 932px; color: var(--white); }
  .rates-head {
    display: flex; font-family: "Oswald", Impact, sans-serif; font-weight: 500;
    font-size: 18px; margin-bottom: 8px;
  }
  .rates-head span:first-child { width: 193px; }
  .rates-row { display: flex; font-size: 14px; line-height: 22.5px; font-weight: 400; }
  .rates-label { width: 193px; }
  .agents { position: absolute; left: 404px; top: 1131px; font-size: 12.5px; line-height: 20px; color: var(--white); }
  .agents b { font-style: italic; font-weight: 700; margin-right: 4px; }
  .contact { position: absolute; left: 608px; top: 1101px; list-style: none; color: var(--white); font-size: 12.5px; line-height: 16px; }
  .contact li { position: relative; padding-left: 14px; margin-bottom: 4px; }
  .contact li::before {
    content: ""; position: absolute; left: 0; top: 4px; width: 7px; height: 7px;
    border-radius: 50%; background: var(--teal);
  }
</style>
</head>
<body>
<main class="flyer">
  <svg class="flyer-shapes" width="869" height="1200" viewBox="0 0 869 1200">
    <defs>
      <linearGradient id="heroTone" x1="0" y1="0" x2="0" y2="1">
        <stop offset="0" stop-color="#2aa7d8"/>
        <stop offset="0.4" stop-color="#8fb9c4"/>
        <stop offset="0.75" stop-color="#4f7a3a"/>
        <stop offset="1" stop-color="#6b6f70"/>
      </linearGradient>
      <linearGradient id="bandTone" x1="0" y1="0" x2="1" y2="0">
        <stop offset="0" stop-color="#158a97"/>
        <stop offset="1" stop-color="#27a2ad"/>
      </linearGradient>
      <linearGradient id="rateTone" x1="0" y1="0" x2="1" y2="0">
        <stop offset="0" stop-color="#1a8e9a"/>
        <stop offset="0.6" stop-color="#11707b"/>
        <stop offset="1" stop-color="#3e4447"/>
      </linearGradient>
      <linearGradient id="harbourTone" x1="0" y1="0" x2="0" y2="1">
        <stop offset="0" stop-color="#4aa3e0"/>
        <stop offset="0.55" stop-color="#b8a88a"/>
        <stop offset="1" stop-color="#1f5f86"/>
      </linearGradient>
      <linearGradient id="promenadeTone" x1="0" y1="0" x2="0" y2="1">
        <stop offset="0" stop-color="#9cc6e4"/>
        <stop offset="0.5" stop-color="#3d83a6"/>
        <stop offset="1" stop-color="#5a5f63"/>
      </linearGradient>
      <linearGradient id="terraceTone" x1="0" y1="0" x2="0" y2="1">
        <stop offset="0" stop-color="#6cb3e0"/>
        <stop offset="0.5" stop-color="#6f8a56"/>
        <stop offset="1" stop-color="#4a4d4f"/>
      </linearGradient>
    </defs>

    <rect x="0" y="0" width="869" height="575" fill="url(#heroTone)" role="img" aria-label="Photo of modern terraced townhouses with balconies and landscaped gardens along a sunny street"/>

    <polygon points="0,348 869,520 869,531 0,360" fill="var(--white)"/>
    <polygon points="0,360 869,531 869,566 0,566" fill="url(#bandTone)"/>
    <polygon points="175,566 869,566 869,583" fill="var(--black)"/>

    <polygon points="0,868 869,948 869,1200 0,1200" fill="url(#rateTone)"/>
    <polygon points="0,862 869,940 869,950 0,874" fill="var(--black)"/>
    <polygon points="185,1200 869,992 869,1200" fill="var(--charcoal)"/>
    <polygon points="163,1200 869,982 869,992 185,1200" fill="var(--white)"/>
    <polygon points="0,1128 160,1200 0,1200" fill="var(--black)"/>
    <polygon points="0,1116 180,1200 160,1200 0,1128" fill="var(--white)"/>

    <polygon points="486,910 540,928 552,1010 520,1106 432,1074 416,990" fill="url(#promenadeTone)" stroke="var(--teal)" stroke-width="6" role="img" aria-label="Photo of a busy waterfront promenade"/>
    <polygon points="577,817 668,846 674,935 616,994 522,966 508,880" fill="url(#harbourTone)" stroke="var(--teal)" stroke-width="6" role="img" aria-label="Photo of a harbour with boats and waterfront buildings"/>
    <polygon points="704,866 800,898 832,985 778,1066 684,1044 646,958" fill="url(#terraceTone)" stroke="var(--teal-deep)" stroke-width="6" role="img" aria-label="Photo of a modern townhouse balcony with garden greenery"/>
  </svg>

  <div class="brand"><span class="brand-dot"></span>HARBOURLINE ESTATES</div>

  <header class="title">
    <h1 class="title-main">TENURE AND</h1>
    <p class="title-sub">OVERSIGHT BUNDLE</p>
  </header>

  <h2 class="includes-heading">INCLUDES</h2>

  <ul class="includes-list col-1">
    <li>Securing Tenant</li>
    <li>Reference/Database<br>Checking</li>
    <li>Lease Preparation<br>and Signing</li>
    <li>Direct Deposit<br>rent collection</li>
    <li>Zero arrears policy<br>management</li>
    <li>Payment of Rates<br>and levies</li>
    <li>Insurance management</li>
  </ul>

  <ul class="includes-list col-2">
    <li>Coordination or all<br>repairs and maintenance</li>
    <li>Regular rent reviews<br>and renewals</li>
    <li>Detailed ingoing, ongoing<br>and outgoing</li>
    <li>Insurance management</li>
    <li>Coordination or all repairs<br>and maintenance</li>
    <li>Regular rent reviews<br>and renewals</li>
    <li>Detailed ingoing, ongoing<br>and outgoing</li>
  </ul>

  <ul class="includes-list col-3">
    <li>Securing Tenant</li>
    <li>Reference/Database<br>Checking</li>
    <li>Lease Preparation<br>and Signing</li>
    <li>Direct Deposit<br>rent collection</li>
    <li>Zero arrears policy<br>management</li>
    <li>Payment of Rates<br>and levies</li>
  </ul>

  <section class="rates">
    <div class="rates-head"><span>Management Rate</span><span>5% + GST – August only</span></div>
    <div class="rates-row"><span class="rates-label">Letting Fee:</span><span>1 weeks rent+GST 6 or 12</span></div>
    <div class="rates-row"><span class="rates-label">Advertising:</span><span>month lease</span></div>
    <div class="rates-row"><span class="rates-label">Professional Photography:</span><span>$350 waived in August</span></div>
    <div class="rates-row"><span class="rates-label">Statements:</span><span>$199 (inc GST) 4 x Photos</span></div>
    <div class="rates-row"><span class="rates-label">Lease Preperation:</span><span>$5.00 Per month</span></div>
    <div class="rates-row"><span class="rates-label">Renewal Fees:</span><span>No Charge</span></div>
    <div class="rates-row"><span class="rates-label"></span><span>½ Weeks Rent +GST</span></div>
  </section>

  <div class="agents">
    <p><b>Liam Carter</b> 0400 000 111</p>
    <p><b>Nadia Rowe</b> 0400 000 222</p>
  </div>

  <ul class="contact">
    <li>Suite 4, 12-14 Shoreline Parade,<br>Seacrest NSW 2099</li>
    <li>hello@harbourlineestates.com.au</li>
    <li>www.harbourlineestates.com.au</li>
  </ul>
</main>
</body>
</html>
```